KTR Associates Business Card

I would like to have a business card designed that uses my current logo and colors. I am not looking for anything to "out there" but can have a little fun so that it stands out.

I have a boutique consulting firm that specializes in strategic planning, change management, leadership development and innovation.

Industry/Entity Type

Leadership

Contact Information for Business Card

Marta Holloway
President
marta@ktr-associates-mail.com
919-555-0143

```html
<!DOCTYPE html>
<html lang="en">
<head>
<meta charset="utf-8">
<title>KTR Associates Business Card</title>
<link rel="stylesheet" href="https://fonts.googleapis.com/css2?family=Open+Sans:ital,wght@0,400;0,600;1,400&display=swap">
<style>
  :root {
    --bg: #ecebe8;
    --paper: #ffffff;
    --ink: #111111;
    --green-dark: #1d7a3c;
    --green-mid: #0d8048;
    --green-lime: #7cc142;
    --white: #ffffff;
  }
  * { margin: 0; padding: 0; box-sizing: border-box; }
  html, body { width: 1200px; height: 873px; overflow: hidden; }
  body {
    background: var(--bg);
    font-family: "Open Sans", Arial, sans-serif;
    position: relative;
  }
  .card {
    position: absolute;
    top: 293px;
    width: 500px;
    height: 286px;
    background: var(--paper);
    overflow: hidden;
    box-shadow: 0 6px 18px rgba(0,0,0,.18);
  }
  .card--contact { left: 70px; }
  .card--brand { left: 630px; }

  .rule { position: absolute; left: 0; right: 0; height: 4px; background: var(--ink); z-index: 2; }
  .rule--top { top: 8px; }
  .rule--bottom { bottom: 8px; }

  .band { position: absolute; }
  .band--dark { left: 0; right: 0; top: 18px; height: 132px; background: var(--green-dark); }
  .band--name { left: 150px; right: 0; top: 34px; height: 62px; background: var(--green-mid); padding: 8px 22px; color: var(--white); }
  .band--contact { left: 40px; right: 90px; top: 96px; height: 42px; background: var(--green-lime); color: var(--white); display: flex; align-items: center; gap: 16px; padding: 0 16px; font-size: 11px; }
  .person-name { font-size: 22px; font-weight: 400; line-height: 1.2; }
  .person-title { font-size: 11px; font-style: italic; }
  .contact-item { display: flex; align-items: center; gap: 6px; white-space: nowrap; }

  .wordmark { position: absolute; color: var(--ink); font-weight: 400; text-align: right; line-height: 1; z-index: 1; }
  .wordmark__name { display: block; }
  .wordmark__suffix { display: block; letter-spacing: .5em; }

  .card--contact .wordmark { right: 34px; top: 172px; }
  .card--contact .wordmark__name { font-size: 52px; }
  .card--contact .wordmark__suffix { font-size: 11px; margin-top: 8px; }

  .green-block { position: absolute; left: 235px; right: 0; top: 128px; bottom: 18px; background: var(--green-dark); }
  .card--brand .wordmark { left: 50px; top: 50px; text-align: left; }
  .card--brand .wordmark__name { font-size: 118px; letter-spacing: -2px; }
  .card--brand .wordmark__suffix { font-size: 13px; margin-top: 14px; margin-left: 4px; }
</style>
</head>
<body>
  <section class="card card--contact" aria-label="Business card, contact side">
    <div class="rule rule--top"></div>
    <div class="band band--dark"></div>
    <div class="band band--name">
      <p class="person-name">Marta Holloway</p>
      <p class="person-title">President</p>
    </div>
    <div class="band band--contact">
      <span class="contact-item">
        <svg width="8" height="13" viewBox="0 0 8 13" aria-hidden="true"><rect x="0.75" y="0.75" width="6.5" height="11.5" rx="1.2" fill="none" stroke="#fff" stroke-width="1.5"/><rect x="3" y="9.5" width="2" height="1.5" fill="#fff"/></svg>
        919-555-0143
      </span>
      <span class="contact-item">
        <svg width="13" height="10" viewBox="0 0 13 10" aria-hidden="true"><rect x="0.75" y="0.75" width="11.5" height="8.5" fill="none" stroke="#fff" stroke-width="1.5"/><path d="M1 1l5.5 4.5L12 1" fill="none" stroke="#fff" stroke-width="1.3"/></svg>
        marta@ktr-associates-mail.com
      </span>
    </div>
    <p class="wordmark">
      <span class="wordmark__name">KTR</span>
      <span class="wordmark__suffix">ASSOCIATES</span>
    </p>
    <div class="rule rule--bottom"></div>
  </section>

  <section class="card card--brand" aria-label="Business card, logo side">
    <div class="rule rule--top"></div>
    <div class="green-block"></div>
    <p class="wordmark">
      <span class="wordmark__name">KTR</span>
      <span class="wordmark__suffix">ASSOCIATES</span>
    </p>
    <div class="rule rule--bottom"></div>
  </section>
</body>
</html>
```